Book Cover: A Quiet Cartographer

DO NOT JUST COPY THE BOOK COVER I HAVE ADDED FOR REFERENCE. I NEED SOMETHING FRESH NOT JUST A COPY AND PASTE!
If you cannot improve on the design with something creative then don't submit a design.

Project Title:
Book Cover Design for A Quiet Cartographer

Must be better than the mock design I have uploaded in project files.

Project Description:
I’m looking for a striking and emotionally evocative book cover for my upcoming title A Quiet Cartographer. This is a deeply personal and powerful memoir about the masks we wear, emotional survival, control, and the journey toward radical self-awareness and healing. The cover should visually represent the contrast between the performative self and the authentic self.

Visual Concept:
Please take visual inspiration and design continuity from my previous book Run FAR Now! — I will upload that cover for reference. This new design should feel like a continuation of the same author journey, but bolder and more psychologically intense.

You’ll be provided with two photos of me:

One where I appear more unkept, raw, and emotionally heavy.

One where I appear clean, centered, and lighter.

These can either be:

Split down the middle to create a “mirror” or duality effect (symbolizing the split self),

Or placed side by side as a subtle before/after or internal/external representation.

You may also consider overlaying or fading one into the other if done tastefully.

The mood should hint at internal conflict, self-reckoning, and healing—but without looking too “self-help cliché.” Think masculine, introspective, modern, and editorial. Avoid overly bright or busy visuals. A minimal or clean design with strong type hierarchy is preferred.

Key Themes to Represent Visually (even abstractly):

Narcissism as a survival mechanism

The emotional cost of performance

The tension between image and authenticity

The healing journey from ego to empathy

Design References:

Run FAR Now! (uploaded) — continuity of brand and typography encouraged

Memoir-style covers like Lanterns Along the Winter Harbour, Saltwater, or A Kettle Hums at Dusk for layout feel

If using color, muted tones with contrast (black/white, sepia, desaturated blues or greys) work well

Title: A Quiet Cartographer
Subtitle (optional placement): Not every narcissist is a monster. Some are just wounded men trying their best to survive
Author: Marlon Weskett

Deliverables:

Full front cover for print sale size as previous cover, including space for subtitle and author name

Spine and back cover (leave placeholder text if no blurb is given)

Ebook cover version

High-resolution files suitable for Quillmark QPS and print use

Additional Notes:
Please ensure the tone stays emotionally resonant, masculine, and sophisticated. No stock image models or cliché therapist symbols. Use my uploaded photos only.

Looking forward to seeing your vision come to life.

Back Cover Blurb – A Quiet Cartographer
A brutally honest recovery story—about what happens after you get clean, and the ego you still have to face.
Most people think addiction ends when you put down the drink, the drug, or the chaos.
But for Marlon Weskett, sobriety was just the start.
Behind the personal development posts, six-pack selfies, and billion-rand property deals, he was still chasing the one thing rehab never took from him: the need to be admired.
This book is not a confession. It’s a dismantling.
In A Quiet Cartographer, Marlon exposes the hidden patterns of ego, control, and validation-seeking that nearly cost him everything—even after he got “better.” With fearless self-inquiry and raw storytelling, he invites readers into his recovery from performance, perfectionism, and power addiction.
Whether you’ve been the narcissist—or you’ve loved one—this book is a mirror. And what you’ll find is not just insight, but a new path forward: one where truth is more powerful than charm, and safety matters more than being impressive.
This isn’t about being perfect.
It’s about being honest.
And finally becoming someone worth trusting—especially by yourself.

Target Market(s)

Any reader wanting to read about narcissism and love

Font styles to use
Sans Serif

Colors
EB3D1F
EC4F4E
F09395
F8D3D4
FCEDEE

Requirements
Must have
• Must be better than the mock design I uploaded.

```html
<!DOCTYPE html>
<html lang="en">
<head>
<meta charset="utf-8">
<title>A Quiet Cartographer — Book Cover</title>
<link href="https://fonts.googleapis.com/css2?family=Oswald:wght@400;500;600;700&family=Open+Sans:ital,wght@0,400;0,600;1,400;1,600;1,700&display=swap" rel="stylesheet">
<style>
  :root{
    --accent:#eb3d1f;
    --coral:#ec4f4e;
    --rose:#f09395;
    --blush:#f8d3d4;
    --paper:#f3efee;
    --charcoal:#161515;
    --spine:#0e0d0d;
    --ink:#2a2727;
    --stone:#cfc9c8;
  }
  *{margin:0;padding:0;box-sizing:border-box}
  html,body{width:1200px;height:823px;overflow:hidden;background:var(--charcoal)}
  .cover{position:relative;width:1200px;height:823px;overflow:hidden;font-family:"Open Sans",sans-serif}

  /* back cover */
  .back{position:absolute;left:0;top:0;width:580px;height:823px;background:var(--paper);color:var(--ink)}
  .back-lead{position:absolute;left:60px;top:66px;width:460px;font-family:"Oswald",sans-serif;font-weight:500;font-size:21px;line-height:29px;text-transform:uppercase;letter-spacing:.5px;color:var(--ink)}
  .back-lead .hl{color:var(--accent)}
  .back-rule{position:absolute;left:60px;top:175px;width:60px;height:3px;background:var(--accent)}
  .back-blurb{position:absolute;left:60px;top:202px;width:460px;font-size:13.2px;line-height:19.6px}
  .back-blurb p{margin-bottom:13px}
  .back-close{font-style:italic;font-weight:700;color:var(--accent)}

  /* spine */
  .spine{position:absolute;left:580px;top:0;width:40px;height:823px;background:var(--spine);
    display:flex;flex-direction:column;align-items:center;justify-content:space-between;padding:34px 0}
  .spine-text{writing-mode:vertical-rl;font-family:"Oswald",sans-serif;text-transform:uppercase;white-space:nowrap;line-height:1}
  .spine-title{color:#fff;font-weight:600;font-size:22px;letter-spacing:2px}
  .spine-mark{width:2px;height:60px;background:var(--accent)}
  .spine-author{color:var(--rose);font-weight:500;font-size:17px;letter-spacing:3px}

  /* front cover */
  .front{position:absolute;left:620px;top:0;width:580px;height:823px;background:var(--charcoal);color:#fff}
  .portrait-raw{position:absolute;left:0;top:0;width:290px;height:540px;
    background:linear-gradient(160deg,#5a5552 0%,#3b3836 55%,#242221 100%)}
  .portrait-clean{position:absolute;left:290px;top:0;width:290px;height:540px;
    background:linear-gradient(200deg,#d6d2d0 0%,#a9a4a2 55%,#6f6b69 100%)}
  .portrait-fade{position:absolute;left:0;top:0;width:580px;height:540px;
    background:linear-gradient(to bottom,rgba(22,21,21,.75) 0%,rgba(22,21,21,0) 18%,rgba(22,21,21,0) 62%,var(--charcoal) 100%)}
  .seam{position:absolute;left:289px;top:96px;width:2px;height:360px;background:var(--accent)}
  .endorsement{position:absolute;left:50px;top:24px;width:480px;text-align:center;font-style:italic;font-size:12.5px;line-height:18px;color:var(--blush)}
  .endorsement .by{font-style:normal;font-weight:600;letter-spacing:1px;color:var(--rose)}
  .title{position:absolute;left:40px;top:440px;font-family:"Oswald",sans-serif;text-transform:uppercase;line-height:1}
  .title-kicker{display:block;font-weight:500;font-size:28px;letter-spacing:10px;color:var(--blush)}
  .title-main{display:block;margin-top:8px;font-weight:700;font-size:72px;letter-spacing:0;color:#fff}
  .front-rule{position:absolute;left:40px;top:582px;width:60px;height:3px;background:var(--accent)}
  .pull-quote{position:absolute;left:40px;top:602px;width:250px;font-style:italic;font-size:13px;line-height:19px;color:var(--stone)}
  .tagline{position:absolute;left:322px;top:602px;width:220px;font-family:"Oswald",sans-serif;font-weight:500;font-size:15px;line-height:24px;letter-spacing:2px;text-transform:uppercase;color:var(--stone)}
  .tagline .key{color:var(--rose)}
  .author{position:absolute;left:40px;top:722px;font-family:"Oswald",sans-serif;font-weight:600;font-size:40px;line-height:1;letter-spacing:8px;text-transform:uppercase;color:#fff}
  .author .last{color:var(--coral)}
</style>
</head>
<body>
<div class="cover">

  <section class="back">
    <p class="back-lead">A brutally honest recovery story—about what happens after you get clean, and <span class="hl">the ego you still have to face.</span></p>
    <div class="back-rule"></div>
    <div class="back-blurb">
      <p>Most people think addiction ends when you put down the drink, the drug, or the chaos. But for Marlon Weskett, sobriety was just the start.</p>
      <p>Behind the personal development posts, six-pack selfies, and billion-rand property deals, he was still chasing the one thing rehab never took from him: the need to be admired. This book is not a confession. It’s a dismantling.</p>
      <p>In A Quiet Cartographer, Marlon exposes the hidden patterns of ego, control, and validation-seeking that nearly cost him everything—even after he got “better.” With fearless self-inquiry and raw storytelling, he invites readers into his recovery from performance, perfectionism, and power addiction.</p>
      <p>Whether you’ve been the narcissist—or you’ve loved one—this book is a mirror. And what you’ll find is not just insight, but a new path forward: <em>one where truth is more powerful than charm, and safety matters more than being impressive.</em></p>
      <p class="back-close">This isn’t about being perfect.<br>It’s about being honest.<br>And finally becoming someone worth trusting—especially by yourself.</p>
    </div>
  </section>

  <section class="spine">
    <span class="spine-text spine-title">A Quiet Cartographer</span>
    <span class="spine-mark"></span>
    <span class="spine-text spine-author">Marlon Weskett</span>
  </section>

  <section class="front">
    <div class="portrait-raw" role="img" aria-label="Left half of the author's face from the raw photo: unkempt, heavy, desaturated and shadowed"></div>
    <div class="portrait-clean" role="img" aria-label="Right half of the author's face from the clean photo: centred, lighter, softly lit in grey tones"></div>
    <div class="portrait-fade"></div>
    <div class="seam"></div>

    <p class="endorsement">“Whatever we’ve been through, Marlon not only makes us feel we can get over it, he gives us the tools to do exactly that.” — <span class="by">RAFE OKONKWO</span></p>

    <h1 class="title">
      <span class="title-kicker">A Quiet</span>
      <span class="title-main">Cartographer</span>
    </h1>
    <div class="front-rule"></div>

    <p class="pull-quote">Not every narcissist is a monster. Some are just wounded men trying their best to survive.</p>

    <p class="tagline">Unmasking the need for<br><span class="key">control, validation</span><br>and <span class="key">being liked</span></p>

    <p class="author">Marlon <span class="last">Weskett</span></p>
  </section>

</div>
</body>
</html>
```